KLR Values Puzzle Pieces

I want to use my logo (symbol only, not the words Marbel Vein Center) as the basis of the puzzle and incorporate our four values into the logo as four puzzle pieces. I want each puzzle piece to have one value on it and a line extending from the piece. At this point, I would like the bullet points of each value to be listed.
Here are the four values with the bullet points:
Cheese Movers
Are open to and embrace change, recognizing that it is a process, not a one-time event.
Are lifelong learners who continually use incremental improvements to enhance their knowledge and skills.
Possess grit, a combination of passion and perseverance, which allows them to overcome challenges and achieve their goals. Grit is the fuel to stay motivated and determined even when faced with obstacles or setbacks.
Are self-disciplined, working smart in thought and action by intentionally focusing on their goals.
Servant-Minded
Approaches work with humility, grace, and mercy, recognizing that serving others is a privilege.
Have a patient-centric approach, looking at the processes through the patient's eyes to ensure the best possible experience.
Educating patients with clarity and consistency, ensuring that they understand vein disease is a treatable but not curable condition.
The "Front Porch Rule" is a guiding principle that everyone is treated with respect, care, and compassion like our beloved family members.
We seek to provide vein care to all who need it.
Better Together
We emphasize the importance of having a team that rows in the same direction towards a common goal.
We have accountability and integrity by taking responsibility for our actions and their impact on others.
We are courageously real, speaking authentically to share thoughts and ideas while feeling valued for our unique perspectives.
We prioritize creating a supportive environment where team members feel they have the resources needed to succeed.
Balanced
We emphasize the importance of maintaining a work-life balance.
We are professional and take what we do seriously while still using laughter and fun to create a welcoming and friendly environment for patients and staff.
Valuable output is the greatest measure, not hours put in. Anyone can keep busy, but that does not equate to productivity.

```html
<!DOCTYPE html>
<html lang="en">
<head>
<meta charset="utf-8">
<title>Our Values Puzzle</title>
<link rel="stylesheet" href="https://fonts.googleapis.com/css2?family=Montserrat:wght@500;700&display=swap">
<style>
  :root {
    --navy: #00137f;
    --green: #00843d;
    --slate: #768594;
    --slate-heading: #5b6b7b;
    --paper: #dfdfdf;
    --ink: #1f1f1f;
    --white: #ffffff;
  }
  html, body {
    margin: 0;
    padding: 0;
    width: 1200px;
    height: 991px;
    overflow: hidden;
    background: var(--paper);
  }
  .values-board {
    position: absolute;
    left: 0;
    top: 95px;
    width: 1850px;
    height: 1233px;
    transform: scale(0.6486);
    transform-origin: 0 0;
    font-family: "Montserrat", sans-serif;
    color: var(--ink);
  }
  .connectors {
    position: absolute;
    left: 0;
    top: 0;
  }
  .value {
    position: absolute;
  }
  .value-title {
    margin: 0;
    font-weight: 700;
    font-size: 40px;
    line-height: 1;
  }
  .value-points {
    list-style: none;
    margin: 0;
    padding: 0;
  }
  .value-points li {
    position: absolute;
    font-weight: 500;
    font-size: 16.4px;
    line-height: 20px;
    white-space: nowrap;
  }
  .value-points li::before {
    content: "";
    position: absolute;
    left: -35px;
    top: 2px;
    width: 16px;
    height: 16px;
    border-radius: 50%;
    background: var(--bullet);
  }
  .value--cheese { --bullet: var(--navy); }
  .value--cheese .value-title { color: var(--navy); }
  .value--servant { --bullet: var(--navy); }
  .value--servant .value-title { color: var(--navy); }
  .value--together { --bullet: var(--green); }
  .value--together .value-title { color: var(--green); }
  .value--balanced { --bullet: var(--slate); }
  .value--balanced .value-title { color: var(--slate-heading); }
</style>
</head>
<body>
<main class="values-board">
  <svg class="connectors" width="1850" height="1233" viewBox="0 0 1850 1233" aria-hidden="true">
    <g fill="none" stroke="var(--white)" stroke-width="7">
      <polyline points="332,134 691,134 774,295"/>
      <polyline points="1473,85 1146,85 1064,283"/>
      <polyline points="201,711 579,711"/>
      <polyline points="1274,718 1614,718"/>
    </g>
    <g class="value-dots" stroke="var(--white)" stroke-width="8">
      <circle cx="332" cy="134" r="25" fill="var(--navy)"/>
      <circle cx="1473" cy="85" r="25" fill="var(--navy)"/>
      <circle cx="201" cy="711" r="25" fill="var(--green)"/>
      <circle cx="1614" cy="718" r="25" fill="var(--slate)"/>
    </g>
    <g class="values-wheel">
      <circle cx="924" cy="618" r="362" fill="var(--white)"/>
      <path d="M916 610 V280 A338 338 0 0 0 586 610 Z" fill="var(--navy)"/>
      <path d="M932 610 V280 A338 338 0 0 1 1262 610 Z" fill="var(--navy)"/>
      <path d="M916 626 V956 A338 338 0 0 1 586 626 Z" fill="var(--green)"/>
      <path d="M932 626 V956 A338 338 0 0 0 1262 626 Z" fill="var(--slate)"/>
    </g>
  </svg>

  <section class="value value--cheese" style="left:121px; top:215px;">
    <h2 class="value-title" style="margin-left:-2px;">Cheese Movers</h2>
    <ul class="value-points">
      <li style="top:53px;">Are open to and embrace change, recognizing that it is<br>a process, not a one-time event.</li>
      <li style="top:133px;">Are lifelong learners who continually use incremental<br>improvements to enhance their knowledge and skills.</li>
      <li style="top:213px;">Possess grit, a combination of passion and perseverance,<br>which allows them to overcome challenges and<br>achieve their goals.<br>Grit is the fuel to stay motivated and determined<br>even when faced with obstacles or setbacks.</li>
      <li style="top:353px;">Are self-disciplined, working smart in thought and<br>action by intentionally focusing on their goals.</li>
    </ul>
  </section>

  <section class="value value--servant" style="left:1336px; top:178px;">
    <h2 class="value-title" style="margin-left:-3px;">Servant-Minded</h2>
    <ul class="value-points">
      <li style="top:59px;">Approaches work with humility, grace, and mercy,<br>recognizing that serving others is a privilege.</li>
      <li style="top:139px;">Have a patient-centric approach, looking at the<br>processes through the patient's eyes to ensure the<br>best possible experience.</li>
      <li style="top:239px;">Educating patients with clarity and consistency,<br>ensuring that they understand vein disease is a<br>treatable but not curable condition.</li>
      <li style="top:339px;">The "Front Porch Rule" is a guiding principle that<br>everyone is treated with respect, care, and compassion<br>like our beloved family members.</li>
      <li style="top:439px;">We seek to provide vein care to all who need it.</li>
    </ul>
  </section>

  <section class="value value--together" style="left:123px; top:783px;">
    <h2 class="value-title" style="margin-left:-2px;">Better Together</h2>
    <ul class="value-points">
      <li style="top:52px;">We emphasize the importance of having a team that rows<br>in the same direction towards a common goal.</li>
      <li style="top:152px;">We have accountability and integrity by taking responsibility<br>for our actions and their impact on others.</li>
      <li style="top:232px;">We are courageously real, speaking authentically to share<br>thoughts and ideas while feeling valued for our unique perspectives.</li>
      <li style="top:332px;">We prioritize creating a supportive environment where team members<br>feel they have the resources needed to succeed.</li>
    </ul>
  </section>

  <section class="value value--balanced" style="left:1294px; top:813px;">
    <h2 class="value-title" style="margin-left:-2px;">Balanced</h2>
    <ul class="value-points">
      <li style="top:58px;">We emphasize the importance of maintaining<br>a work-life balance.</li>
      <li style="top:135px;">We are professional and take what we do seriously while<br>still using laughter and fun to create a welcoming and<br>friendly environment for patients and staff.</li>
      <li style="top:233px;">Valuable output is the greatest measure, not hours put in.<br>Anyone can keep busy, but that does not equate to<br>productivity.</li>
    </ul>
  </section>
</main>
</body>
</html>
```